Brochure for handout and mailing

we market directly to small retail businesses. We provide personal attention to our clients to customize their applications to the lenders requirements. Small business owners do not have time to apply to the hundreds of lenders. We know which lenders are appropriate for your particular business. we make sure our clients are protected from unscrupulous lenders that lend money at rates that will damage a business. We really care about the ultimate success of our clients. we ant them to become a partner for years to come. One application will go to 5 hand picked lenders. We have a fast and secure online application. Funding in 7 days. Loan terms from 6 months to 5 years. Loan rates from 4% to 19%. Broker fees from 1% to 5%. We are a small family business ourselves with over 30 years experience. Integrity - Transparency. (we are not committed to the logo) (just designed it on Printolux.) would like to convert design to html or pdf version for email campaign also. Required Trifold Brochures (10.98" x 8.5"). I will be using printolux. They have a Brochure Template you can download.

Target Market(s)

Small Business Owners in the US

Industry/Entity Type

Retail

Font styles to use
Sans Serif

Colors
3176b5
85acd3
86cfc6

Requirements
Must have
• Full Bleed Size (starting document size)
• 11.10" x 8.63"
• 282 x 219 mm
• 3331 x 2588 pixels
• * Finished artwork should use the full bleed dimensions for best results.
• Document Trim Size (final size after being cut)
• 10.98" x 8.50"
• 279 x 216 mm
• 3295 x 2551 pixels
• * Please be sure to keep all text within the safe margin.
• Resolution
• 300 DPI
• * Dotted lines indicate where a fold will take place. If you don’t want copy or design to appear on the fold, make sure they stay within each panel’s safe margin. See full upload specifications at Printolux / brochures
Nice to have
• see www.quarrafundhub.com

```html
<!DOCTYPE html>
<html lang="en">
<head>
<meta charset="utf-8">
<title>QuarraFundHub Trifold Brochure</title>
<link rel="stylesheet" href="https://fonts.googleapis.com/css2?family=Roboto:wght@300;400;500;700;900&family=Roboto+Condensed:wght@300;400;700&display=swap">
<style>
  :root {
    --cyan: #1bb5ec;
    --cyan-deep: #1aa3dd;
    --pink: #f28c8c;
    --navy: #1a6fb0;
    --green: #5db847;
    --white: #ffffff;
    --ink: #56585b;
  }
  html, body { margin: 0; padding: 0; overflow: hidden; background: #ffffff; }
  .brochure {
    position: relative; width: 1200px; height: 928px; overflow: hidden;
    font-family: "Roboto", Arial, sans-serif; background: var(--white);
  }
  .backdrop { position: absolute; inset: 0; }
  .abs { position: absolute; margin: 0; }

  .top-brand {
    left: 440px; top: 32px; font-size: 27px; font-weight: 900; line-height: 32px;
    color: var(--green); letter-spacing: 0.5px; display: flex; align-items: center; gap: 10px;
  }
  .top-brand .dot { width: 28px; height: 28px; border-radius: 50%; background: var(--green); }

  .about-tag {
    left: 131px; top: 140px; width: 152px; height: 61px; background: var(--white);
    box-shadow: 2px 3px 6px rgba(0,0,0,0.25);
    font-size: 32px; font-weight: 300; color: var(--ink);
    display: flex; align-items: center; justify-content: center;
  }
  .about-copy {
    left: 41px; width: 320px; color: var(--white);
    font-size: 13.2px; line-height: 18.8px; text-align: justify;
  }
  .about-copy p { margin: 0 0 18px; }
  .about-copy strong { font-weight: 700; }
  .about-intro { top: 228px; }
  .about-more { top: 662px; }

  .store-photo { left: 0; top: 395px; width: 366px; height: 256px; }

  .rates {
    left: 550px; top: 404px; width: 200px; text-align: right;
    font-family: "Roboto Condensed", Arial, sans-serif;
  }
  .rates .label { font-family: "Roboto", Arial, sans-serif; font-weight: 300; font-size: 36px; color: var(--pink); line-height: 40px; letter-spacing: -0.5px; }
  .rates .range { font-size: 25px; color: var(--navy); line-height: 28px; margin-bottom: 16px; }
  .rates .family { font-size: 14.5px; line-height: 16px; color: var(--navy); }
  .rates .family .accent { color: var(--pink); }
  .rates-rule { left: 758px; top: 400px; width: 0; height: 226px; border-left: 1px solid var(--cyan); }

  .address {
    left: 440px; top: 798px; width: 320px; text-align: center;
    color: var(--white); font-size: 17px; line-height: 19px;
  }
  .address .tag { color: var(--pink); }

  .brand-name {
    left: 800px; top: 180px; width: 400px; text-align: center;
    font-size: 30px; font-weight: 700; color: #17406b; letter-spacing: 0.5px;
  }
  .know-box {
    left: 922px; top: 235px; width: 169px; height: 124px; background: var(--pink);
    box-shadow: 2px 3px 6px rgba(0,0,0,0.2);
    color: var(--white); text-align: center; line-height: 30px;
    display: flex; flex-direction: column; justify-content: center;
  }
  .know-box .light { font-size: 30px; font-weight: 300; }
  .know-box .bold { font-size: 32px; font-weight: 700; }

  .specialize { left: 820px; top: 393px; width: 360px; text-align: center; color: var(--cyan-deep); }
  .specialize .line1 { font-size: 26px; font-weight: 400; }
  .specialize .line2 { font-size: 38px; line-height: 40px; font-weight: 400; }
  .specialize .line3 { font-size: 38px; line-height: 40px; font-weight: 400; }
  .specialize b { color: var(--navy); font-weight: 700; }

  .feature {
    left: 906px; width: 176px; border: 1px solid var(--cyan); text-align: center;
    color: var(--navy); background: var(--white); padding: 2px 0 3px;
    font-family: "Roboto Condensed", Arial, sans-serif; white-space: nowrap;
  }
  .feature .big { font-size: 22px; line-height: 23px; }
  .feature .big .hl { color: var(--cyan-deep); }
  .feature .small { font-size: 10.5px; line-height: 12px; font-weight: 700; color: var(--cyan-deep); }
  .feature-fast { top: 509px; }
  .feature-fund { top: 556px; }

  .web { left: 844px; top: 866px; font-size: 20px; font-weight: 700; color: var(--white); }
  .web .tag { color: var(--pink); font-weight: 400; }
</style>
</head>
<body>
<div class="brochure">
  <svg class="backdrop" width="1200" height="928" viewBox="0 0 1200 928" aria-hidden="true">
    <defs>
      <linearGradient id="chefTone" x1="0" y1="0" x2="0" y2="1">
        <stop offset="0" stop-color="#8a7667"/><stop offset="1" stop-color="#d9d2c8"/>
      </linearGradient>
      <linearGradient id="shopTone" x1="0" y1="0" x2="0" y2="1">
        <stop offset="0" stop-color="#b3966a"/><stop offset="1" stop-color="#e6d8c2"/>
      </linearGradient>
    </defs>
    <rect width="1200" height="928" fill="var(--cyan)"/>
    <path d="M0,0 H1200 V515 C1060,555 900,640 800,730 C640,700 540,640 535,540 C530,440 570,380 660,330 C740,285 790,250 805,195 C600,95 300,65 0,62 Z" fill="var(--white)"/>
    <path d="M0,52 C300,55 600,85 810,188" fill="none" stroke="var(--pink)" stroke-width="18"/>
    <path d="M535,560 C530,440 570,380 660,330 C740,285 790,250 808,192" fill="none" stroke="var(--pink)" stroke-width="8"/>
    <path d="M800,0 H1200 V30 C1080,20 900,14 800,0 Z" fill="var(--pink)"/>
    <path d="M800,730 C900,640 1060,555 1200,515 V600 C1060,615 920,675 822,745 Z" fill="var(--pink)"/>
    <circle cx="575" cy="274" r="92" fill="var(--pink)"/>
    <circle cx="575" cy="274" r="74" fill="none" stroke="var(--white)" stroke-width="3"/>
    <circle cx="1040" cy="732" r="112" fill="var(--cyan)"/>
    <circle cx="1040" cy="732" r="92" fill="none" stroke="var(--white)" stroke-width="3"/>
    <circle cx="575" cy="274" r="68" fill="url(#chefTone)" role="img" aria-label="Photo of a chef presenting a plated dish in a restaurant kitchen"/>
    <circle cx="1040" cy="732" r="86" fill="url(#shopTone)" role="img" aria-label="Photo of two shop owners holding an open sign in their store"/>
    <rect x="0" y="395" width="366" height="256" fill="url(#shopTone)" role="img" aria-label="Photo of a smiling couple standing outside their organic produce shop"/>
  </svg>

  <div class="abs top-brand"><span class="dot"></span>QUARRAFUNDHUB</div>

  <div class="abs about-tag">About Us</div>
  <div class="abs about-copy about-intro">
    <p><strong>QuarraFundHub</strong> is the only company of its kind. We are a small, family business with over 30 years of experience. We were founded on the principle that small business is the heart and soul of American capitalism. It is also a necessary component of a free society. To be successful, small businesses must have easy access to many and varied financial resources in one place.</p>
  </div>
  <div class="abs about-copy about-more">
    <p>While utilizing all the advantages of advanced technology, we strongly believe that only with personal attention can your business be successfully represented to lenders.</p>
    <p>We get to know you and your unique requirements. We match those requirements with the lenders requirements.</p>
    <p>We are a hybrid of state of the art technology and dedicated, personal attention.</p>
  </div>

  <div class="abs rates">
    <div class="label">Loan Rates</div>
    <div class="range">from 4% to 19%</div>
    <div class="label">Broker Fees</div>
    <div class="range">from 1% to 5%</div>
    <div class="family">We are a small family business<br>ourselves with<br>over <span class="accent">30 years Experience.</span><br>Integrity - Transparency</div>
  </div>
  <div class="abs rates-rule"></div>

  <div class="abs address">
    418 Harlow Ave Suite<br>
    12-208 Crestmoor Bay, NV 89502<br>
    <span class="tag">T:</span> 800-555-0142<br>
    <span class="tag">F:</span> 866-555-0187<br>
    <span class="tag">E:</span> info@quarrafundhub.com
  </div>

  <div class="abs brand-name">QuarraFundHub</div>
  <div class="abs know-box">
    <span class="light">We Know</span>
    <span class="bold">Small</span>
    <span class="bold">Business</span>
  </div>
  <div class="abs specialize">
    <div class="line1">We specialize in Securing:</div>
    <div class="line2"><b>LOANS</b> For</div>
    <div class="line3">SMALL <b>BUSINESSES</b></div>
  </div>
  <div class="abs feature feature-fast">
    <div class="big">Fast &amp; <span class="hl">Secure</span></div>
    <div class="small">ONLINE APPLICATION</div>
  </div>
  <div class="abs feature feature-fund">
    <div class="big">Funding in <span class="hl">7 DAYS</span></div>
    <div class="small">Loan terms from 6 MONTHS - 5 YEARS</div>
  </div>

  <div class="abs web"><span class="tag">W:</span> www.quarrafundhub.com</div>
</div>
</body>
</html>
```